Rewards Program

I would logo a Rewards Card designed that looks similar to a credit card. I am attaching my KALTO logo, and also a sample rewards card that I liked. I open to the background being Silver or Black and really like the Brevanta logo at the bottom as well.

Credit Card

```html
<!DOCTYPE html>
<html lang="en">
<head>
<meta charset="utf-8">
<title>KALTO Reward Card</title>
<link href="https://fonts.googleapis.com/css2?family=Share+Tech+Mono&family=Roboto+Condensed:wght@400;700&family=Roboto+Mono:wght@400&display=swap" rel="stylesheet">
<style>
  :root {
    --page: #ffffff;
    --card-light: #fbfbfb;
    --card-mid: #e9e9e9;
    --ink: #111111;
    --emboss-face: #f2f2f2;
    --emboss-dark: #6f6f6f;
    --brand: #e0141c;
  }
  * { margin: 0; padding: 0; box-sizing: border-box; }
  html, body { width: 916px; height: 1200px; overflow: hidden; background: var(--page); }
  .canvas { position: relative; width: 916px; height: 1200px; }

  .reward-card {
    position: absolute;
    left: 153px;
    width: 614px;
    height: 388px;
    border-radius: 16px;
    border: 1px solid #d2d2d2;
    box-shadow: 0 3px 4px rgba(0,0,0,0.35);
    overflow: hidden;
  }
  .reward-card--classic { top: 127px; }
  .reward-card--lined { top: 611px; }

  .card-surface {
    position: absolute; inset: 0;
    background: linear-gradient(160deg, var(--card-light) 0%, var(--card-mid) 55%, var(--card-light) 100%);
  }

  .card-title { position: absolute; color: var(--ink); font-weight: 400; white-space: nowrap; }
  .reward-card--classic .card-title {
    right: 37px; top: 45px;
    font-family: "Roboto Condensed", sans-serif;
    font-size: 62px; line-height: 45px; text-align: right;
  }
  .reward-card--lined .card-title-main {
    left: 68px; top: 28px;
    font-family: "Roboto Mono", monospace;
    font-size: 72px; line-height: 60px; letter-spacing: 11px;
  }
  .reward-card--lined .card-title-sub {
    left: 353px; top: 93px;
    font-family: "Roboto Mono", monospace;
    font-size: 54px; line-height: 50px; letter-spacing: 12px;
  }
  .title-rule {
    position: absolute; left: 53px; top: 90px;
    width: 502px; height: 3px; background: var(--ink);
  }

  .embossed {
    position: absolute;
    font-family: "Share Tech Mono", monospace;
    color: var(--emboss-face);
    text-shadow: 1px 1px 0 var(--emboss-dark), 2px 2px 0 #9a9a9a, -1px -1px 0 #ffffff;
    -webkit-text-stroke: 0.6px #8a8a8a;
    white-space: nowrap;
  }
  .card-number { left: 44px; font-size: 40px; letter-spacing: 3.5px; }
  .card-code, .card-expiry { font-size: 34px; letter-spacing: 6px; }
  .card-code { left: 47px; }
  .card-expiry { left: 251px; }
  .reward-card--classic .card-number { top: 204px; }
  .reward-card--classic .card-code,
  .reward-card--classic .card-expiry { top: 302px; }
  .reward-card--lined .card-number { top: 212px; font-size: 37px; letter-spacing: 3px; }
  .reward-card--lined .card-code,
  .reward-card--lined .card-expiry { top: 270px; }

  .brand-tile {
    position: absolute; width: 127px; height: 77px;
    background: #ffffff; border: 1px solid #dcdcdc;
    display: flex; align-items: center; justify-content: center;
    font-family: "Roboto Condensed", sans-serif; font-weight: 700;
    font-size: 30px; color: var(--brand); letter-spacing: 0.5px;
  }
  .reward-card--classic .brand-tile { left: 460px; top: 289px; }
  .reward-card--lined .brand-tile { left: 460px; top: 291px; }
</style>
</head>
<body>
<main class="canvas">

  <section class="reward-card reward-card--classic">
    <div class="card-surface" role="img" aria-label="Soft silver card surface with a faint wave texture"></div>
    <h2 class="card-title">REWARD<br>CARD</h2>
    <p class="embossed card-number">1234 5674 5678 1235</p>
    <p class="embossed card-code">0000</p>
    <p class="embossed card-expiry">00/00</p>
    <div class="brand-tile">KALTO</div>
  </section>

  <section class="reward-card reward-card--lined">
    <div class="card-surface" role="img" aria-label="Soft silver card surface with a faint wave texture"></div>
    <h2 class="card-title card-title-main">REWARD</h2>
    <div class="title-rule"></div>
    <p class="card-title card-title-sub">CARD</p>
    <p class="embossed card-number">1234 5674 5678 1235</p>
    <p class="embossed card-code">0000</p>
    <p class="embossed card-expiry">00/00</p>
    <div class="brand-tile">KALTO</div>
  </section>

</main>
</body>
</html>
```